Newsletter-Design für Garten-Samen Shop
Zielgruppe
Online Shop für Obst-, Gemüse-, Kräuter- und Pflanzensamen
Aufgabenstellung
www.beetfreunde-portal.example ist die Seite mit den Produkten. Als Tipp sollte das Jiaogulan genannt werden da dieses Produkt sich am meisten verkauft.

```html
<!DOCTYPE html>
<html lang="de">
<head>
<meta charset="utf-8">
<title>Flyer – Beetfreunde Portal</title>
<link rel="stylesheet" href="https://fonts.googleapis.com/css2?family=Open+Sans:wght@300;400;600&display=swap">
<style>
  :root {
    --canvas-bg: #e6e6e8;
    --leaf-green: #8fcb98;
    --banner-green: #a8dcae;
    --white: #ffffff;
    --veg-pale: #e4ecd2;
    --veg-green: #b8d39a;
    --veg-orange: #e9834a;
    --veg-red: #c94a48;
    --herb-dark: #5f9a5a;
    --herb-light: #b9dfb0;
  }
  html, body {
    margin: 0;
    padding: 0;
    width: 1200px;
    height: 848px;
    overflow: hidden;
    background: var(--canvas-bg);
    font-family: "Open Sans", sans-serif;
  }
  .canvas {
    position: relative;
    width: 1200px;
    height: 848px;
  }
  .flyer {
    position: absolute;
    left: 331px;
    top: 44px;
    width: 538px;
    height: 760px;
    box-shadow: 0 6px 24px rgba(0,0,0,0.18);
  }
  .flyer svg { display: block; }
  .headline {
    font-weight: 400;
    font-size: 25px;
    fill: var(--white);
    letter-spacing: 0.5px;
  }
  .tip-label {
    font-weight: 300;
    font-size: 17px;
    fill: var(--white);
  }
  .product-name {
    font-weight: 400;
    font-size: 25px;
    fill: var(--white);
  }
  .product-tagline {
    font-weight: 400;
    font-size: 12px;
    fill: var(--white);
  }
  .product-copy {
    font-weight: 400;
    font-size: 11.5px;
    fill: var(--white);
  }
  .shop-url {
    font-weight: 600;
    font-size: 22px;
    fill: var(--white);
  }
  .shop-claim {
    font-weight: 400;
    font-size: 11.5px;
    fill: var(--white);
  }
</style>
</head>
<body>
<div class="canvas">
  <div class="flyer">
    <svg width="538" height="760" viewBox="0 0 538 760" xmlns="http://www.w3.org/2000/svg">
      <defs>
        <linearGradient id="vegGradient" x1="0" y1="0" x2="0.55" y2="1">
          <stop offset="0" stop-color="var(--veg-pale)"/>
          <stop offset="0.3" stop-color="var(--veg-green)"/>
          <stop offset="0.55" stop-color="var(--veg-orange)"/>
          <stop offset="0.85" stop-color="var(--veg-red)"/>
        </linearGradient>
        <radialGradient id="herbGradient" cx="0.5" cy="0.45" r="0.6">
          <stop offset="0" stop-color="var(--herb-light)"/>
          <stop offset="1" stop-color="var(--herb-dark)"/>
        </radialGradient>
        <path id="tipArc" d="M 330 420 A 82 82 0 0 0 372 330"/>
      </defs>

      <!-- produce photo area -->
      <rect class="produce-photo" x="0" y="0" width="538" height="760" fill="url(#vegGradient)"
            role="img" aria-label="Foto mit frischem Obst und Gemüse: Lauch, Brokkoli, Karotten und ein roter Apfel"/>

      <!-- green lower area with one continuous curve -->
      <path class="green-field" d="M 0 760 L 0 660 C 70 460, 250 325, 538 335 L 538 760 Z" fill="var(--leaf-green)"/>

      <!-- outline frame -->
      <rect x="40" y="105" width="458" height="600" fill="none" stroke="var(--white)" stroke-width="1.5"/>

      <!-- headline banner -->
      <rect x="28" y="52" width="470" height="110" fill="var(--banner-green)" opacity="0.95"/>
      <rect x="38" y="62" width="450" height="90" fill="none" stroke="var(--white)" stroke-width="1.2"/>
      <text class="headline" x="263" y="100" text-anchor="middle">Das beste Obst und Gemüse</text>
      <text class="headline" x="263" y="134" text-anchor="middle">kommt aus dem eigenen Garten</text>

      <!-- herb tip circle -->
      <circle class="herb-photo" cx="300" cy="370" r="68" fill="url(#herbGradient)" stroke="var(--white)" stroke-width="3"
              role="img" aria-label="Foto der Jiaogulan-Pflanze mit grünen Blättern"/>
      <text class="tip-label"><textPath href="#tipArc" startOffset="8%">Unser Tipp!</textPath></text>

      <!-- product text -->
      <text class="product-name" x="70" y="485">Jiaogulan</text>
      <text class="product-tagline" x="76" y="507">- Das Kraut der Unsterblichkeit</text>
      <text class="product-copy" x="76" y="535">Das Superfood verbessert die Nährstoff-</text>
      <text class="product-copy" x="76" y="552">versorgung aller Organe, sowie die</text>
      <text class="product-copy" x="76" y="569">Herzleistung und die Blutzirkulation.</text>

      <!-- shop info -->
      <text class="shop-url" x="290" y="630" text-anchor="middle">beetfreunde-portal.example</text>
      <text class="shop-claim" x="290" y="655" text-anchor="middle">Ihr Onlineshop für Obst-,</text>
      <text class="shop-claim" x="290" y="671" text-anchor="middle">Gemüse-, Kräuter- und</text>
      <text class="shop-claim" x="290" y="687" text-anchor="middle">Pflanzensamen</text>
    </svg>
  </div>
</div>
</body>
</html>
```